Website Redesign - We Need Your Magic!

Hello we are looking for you to help us re-design a high end and professional website for a high-end private school.

Here is the current site: http://www.brevanholt.example/

NOTE THIS IS DESIGN ONLY, NO CODING :)

The image they want to portray is that of high quality sports and education, in a creative "un-stiff" way.

Menu Bar: Horizontal

Look and Feel:

Site Colors: Dark green and a Gold yellow (logos are attached)

This site will represent a school so the look must be clean, bold, and classy. The site must have a very clean user interface, with things easily recognizable. Think simple.

The site should be visually appealing! If you come to me with templates, or a ton of text you will be out.

This site should be outside the box, we do not want boring, we do not want status quo. This site should instill excitement, innovation, and athletics.

So the main points again are:

1. High-end and classy look, with creative feel
2. Simple and clear navigation style
3. To cover the Junior and High School - Brevanholt College Schools

Think outside the box. We look forward to seeing what you come up with!!

Thank you for helping us create an amazing site for the school!

Industry/Entity Type

School

```html
<!DOCTYPE html>
<html lang="en">
<head>
<meta charset="utf-8">
<title>Brevanholt College</title>
<link href="https://fonts.googleapis.com/css2?family=Oswald:wght@400;500&family=Open+Sans:wght@400;600&display=swap" rel="stylesheet">
<style>
:root{
  --green:#0b5121;
  --green-mid:#11602a;
  --green-row:#0f5a26;
  --green-row-alt:#0a4a1d;
  --green-panel:#1c6f31;
  --green-footer:#0d4b1f;
  --green-base:#083a17;
  --gold:#f6e514;
  --white:#ffffff;
  --line:#2a7a3d;
}
*{margin:0;padding:0;box-sizing:border-box}
html,body{width:1200px;height:2769px;overflow:hidden}
body{background:var(--green);color:var(--white);font-family:'Open Sans',sans-serif;position:relative}
.abs{position:absolute}
h2{font-family:'Oswald',sans-serif;font-weight:500;font-size:22px;text-transform:uppercase;letter-spacing:.3px;line-height:1;white-space:nowrap}
h2 span{color:var(--gold)}
h2::after{content:"";display:block;width:46px;height:4px;background:var(--gold);margin-top:9px}
p{font-size:12.5px;line-height:22px}

/* header */
.brand{left:166px;top:12px;width:80px;height:104px;display:flex;flex-direction:column;align-items:center;justify-content:center;gap:8px}
.brand-dot{width:58px;height:58px;background:var(--gold);border-radius:50%}
.brand-name{font-family:'Oswald',sans-serif;font-weight:500;font-size:13px;color:var(--gold);letter-spacing:.5px;white-space:nowrap}
.info{left:653px;top:26px;display:flex;gap:10px;align-items:center}
.info small{display:block;font-size:10px;font-weight:600;text-transform:uppercase}
.info strong{display:block;font-family:'Oswald',sans-serif;font-weight:500;color:var(--gold);font-size:24px;line-height:1.1}
.search{left:865px;top:26px}
.search small{font-size:10px;font-weight:600;text-transform:uppercase;display:block;margin-bottom:5px}
.search .field{width:176px;height:24px;background:var(--white);color:#777;font-size:10px;padding:5px 8px;position:relative}
.search svg{position:absolute;right:6px;top:6px}
.nav{left:355px;top:93px;display:flex;gap:27px;font-family:'Oswald',sans-serif;font-size:13px;text-transform:uppercase}
.nav a{color:var(--white);text-decoration:none;padding-bottom:5px}
.nav a.active{border-bottom:2px solid var(--white)}

/* hero grid */
.hero{left:0;top:143px;width:1200px;height:475px;display:grid;grid-template-columns:repeat(5,240px);grid-template-rows:238px 237px}
.tile{display:block}

/* welcome */
.welcome h2{left:162px;top:664px;position:absolute}
.welcome-text{left:162px;top:712px;width:500px}
.welcome-text p+p{margin-top:14px}
.video{left:688px;top:669px;width:351px;height:231px;border:3px solid var(--green-panel);background:linear-gradient(#8b9a7e,#5d6b4e 55%,#6e7b3a)}
.video .play{position:absolute;left:50%;top:50%;transform:translate(-50%,-50%)}
.rule{left:162px;width:876px;height:1px;background:var(--line)}

/* notes */
.note h2{position:absolute}
.note .photo{position:absolute;width:148px;height:146px;border:3px solid var(--green-panel)}
.note p{position:absolute;font-size:11.5px;line-height:19.5px}
.more{position:absolute;background:var(--green-base);border:1px solid var(--line);color:var(--gold);font-size:11px;font-weight:600;padding:4px 11px}

/* calendar */
.cal-title{left:162px;top:1347px}
.cal{left:162px;top:1400px;width:876px;border-collapse:collapse;font-size:11.5px}
.cal th{font-family:'Oswald',sans-serif;font-weight:500;color:var(--gold);font-size:15px;text-transform:uppercase;height:48px;text-align:center}
.cal td{text-align:center;padding:4px 0;line-height:17px}
.cal tbody tr{height:54px}
.cal tbody tr:nth-child(odd){background:var(--green-row)}
.cal tbody tr:nth-child(even){background:var(--green-row-alt)}
.cal td.label{text-align:left;padding-left:14px;font-family:'Oswald',sans-serif;font-size:15px;text-transform:uppercase;width:205px}
.btn-gold{position:absolute;top:1793px;width:276px;height:46px;background:var(--gold);color:#13351b;font-family:'Oswald',sans-serif;font-size:14px;text-transform:uppercase;display:flex;align-items:center;justify-content:center}

/* events */
.events-title{left:162px;top:1917px}
.event{position:absolute;top:1973px;width:200px}
.event .pic{height:128px;border:3px solid var(--green-panel)}
.event h3{font-family:'Oswald',sans-serif;font-weight:400;font-size:16px;margin-top:24px;text-transform:uppercase}
.event p{font-size:12px;line-height:20px;margin-top:4px}
.sports-title{left:835px;top:1917px}
.sports{left:835px;top:1975px;list-style:none;font-size:12.5px;line-height:42px}
.partner{position:absolute;top:2257px;width:148px;height:90px;background:var(--white);display:flex;align-items:center;justify-content:center}

/* footer */
.footer{left:0;top:2407px;width:1200px;height:323px;background:var(--green-footer)}
.base{left:0;top:2730px;width:1200px;height:39px;background:var(--green-base)}
.contact{position:absolute;width:190px;text-align:center;font-size:11px;line-height:17px}
.contact .ic{width:34px;height:34px;margin:0 auto 8px;background:var(--gold);border-radius:50%;display:flex;align-items:center;justify-content:center}
.contact b{color:var(--gold);font-weight:600;display:block;text-transform:uppercase}
.feed{left:535px;top:2520px;width:203px;height:180px;background:var(--white);color:#333;font-size:9px;padding:8px}
.feed .head{display:flex;gap:6px;align-items:center;font-weight:600;color:#2d4a8a;font-size:10px}
.feed .sq{width:26px;height:26px;background:var(--green)}
.feed .like{margin-top:10px;border-top:1px solid #ddd;padding-top:6px}
.feed .faces{display:grid;grid-template-columns:repeat(5,30px);gap:6px;margin-top:8px}
.feed .faces i{height:30px;background:#9aa3ad;display:block}
.signup{left:762px;top:2397px;width:276px;height:333px;background:var(--green-panel);padding:40px 23px 0}
.signup p{font-size:11px;line-height:18px;margin-top:18px}
.signup .input{width:230px;height:28px;background:var(--white);color:#555;font-size:10px;padding:7px 9px;margin-top:16px}
.signup .input+.input{margin-top:18px}
.signup .actions{display:flex;gap:14px;margin-top:18px}
.signup .actions span{width:108px;height:27px;display:flex;align-items:center;justify-content:center;font-family:'Oswald',sans-serif;font-size:12px;text-transform:uppercase}
.sub{background:var(--gold);color:#13351b}
.unsub{background:var(--green-base);color:var(--white)}
.copy{left:162px;top:2741px;font-size:11px}
.social{left:957px;top:2738px;display:flex;gap:6px}
.social i{width:22px;height:22px;border-radius:50%;background:var(--green-panel);display:block}
</style>
</head>
<body>

<header>
  <div class="abs brand"><span class="brand-dot"></span><span class="brand-name">BREVANHOLT</span></div>
  <div class="abs info">
    <svg width="22" height="30" viewBox="0 0 22 30"><rect x="1" y="1" width="20" height="28" rx="3" fill="none" stroke="#fff" stroke-width="2"/><rect x="5" y="5" width="12" height="14" fill="#fff"/><circle cx="11" cy="24" r="2" fill="#fff"/></svg>
    <div><small>Information Call</small><strong>0771830462</strong></div>
  </div>
  <div class="abs search">
    <small>Search Now!</small>
    <div class="field">Enter Your Keyword...<svg width="12" height="12" viewBox="0 0 12 12"><circle cx="5" cy="5" r="3.5" fill="none" stroke="#555" stroke-width="1.5"/><line x1="7.5" y1="7.5" x2="11" y2="11" stroke="#555" stroke-width="1.5"/></svg></div>
  </div>
  <nav class="abs nav">
    <a class="active">Home</a><a>About</a><a>Academics</a><a>Sports</a><a>Joining Brevanholt</a><a>Working at the College</a><a>Contact</a>
  </nav>
</header>

<section class="abs hero">
  <span class="tile" role="img" aria-label="Rider jumping a horse over a fence" style="background:linear-gradient(#4f6f3a,#6e8a4e)"></span>
  <span class="tile" role="img" aria-label="Girls playing netball on a court" style="background:linear-gradient(#9a7a5a,#b0643f)"></span>
  <span class="tile" role="img" aria-label="Boys playing football on a field" style="background:linear-gradient(#7a8a6a,#4d7a32)"></span>
  <span class="tile" role="img" aria-label="Runners crossing the finish line" style="background:linear-gradient(#6a8050,#5e7040)"></span>
  <span class="tile" role="img" aria-label="Pupil in a dormitory room" style="background:linear-gradient(#b8a890,#3f6a3a)"></span>
  <span class="tile" role="img" aria-label="Tree-lined campus path" style="background:linear-gradient(#4d6e3a,#7a7a60)"></span>
  <span class="tile" role="img" aria-label="Students in blazers talking outdoors" style="background:linear-gradient(#5a7a4a,#2f5a2f)"></span>
  <span class="tile" role="img" aria-label="Group of pupils gathered together" style="background:linear-gradient(#8a7a6a,#3a3a3a)"></span>
  <span class="tile" role="img" aria-label="Open playing fields" style="background:linear-gradient(#9aa890,#5c7a3e)"></span>
  <span class="tile" role="img" aria-label="Pupil in a science laboratory" style="background:linear-gradient(#c8c4bc,#8a8a86)"></span>
</section>

<section class="welcome">
  <h2>Welcome to <span>Brevanholt College</span></h2>
  <div class="abs welcome-text">
    <p>Welcome to Brevanholt Group of Schools where our School Motto is 'Tabatana' meaning Togetherness. We aim to work together in every aspect of School life, from academics to sport. Brevanholt College opened on 14th February 1983 and occupies 120 ha of land amidst the low hills of the Marrow Range, 8km west of Kestrelby. This location encourages focus on School life away from the distractions and hustle and bustle of the larger towns.</p>
    <p>The day scholars have the option of selected bus drop off points for parents to collect day scholars closer to home. Brevanholt College offers a wide range of academic subjects alongside a varied sport and extra-curricular program.</p>
  </div>
  <div class="abs video" role="img" aria-label="Video still of the college entrance building">
    <svg class="play" width="58" height="58" viewBox="0 0 58 58"><circle cx="29" cy="29" r="27" fill="none" stroke="#fff" stroke-width="3"/><polygon points="23,17 23,41 42,29" fill="#fff"/></svg>
  </div>
</section>

<div class="abs rule" style="top:946px"></div>

<section class="note">
  <h2 style="left:162px;top:992px">Headmaster's <span>Welcome Note</span></h2>
  <div class="photo" role="img" aria-label="Portrait of the headmaster" style="left:162px;top:1048px;background:linear-gradient(#7a8a6a,#3a4a5a)"></div>
  <p style="left:342px;top:1042px;width:236px">Welcome to Brevanholt College. Here at the College we aim to encourage each pupil to be a self-confident, well-rounded individual. We aim to propel them to the highest level of achievement in both academics and extra-curricular activities to provide them with the life skills they will need when they leave the College and to prepare them to be of value to society.</p>
  <span class="more" style="left:337px;top:1234px">Read More</span>

  <h2 style="left:623px;top:992px">Memorial Garden <span>Opened Speech Day 2011</span></h2>
  <div class="photo" role="img" aria-label="Pupils standing at the memorial garden" style="left:625px;top:1048px;background:linear-gradient(#5a7a4a,#3a4a3a)"></div>
  <p style="left:798px;top:1042px;width:242px">Every year the Lower Sixes choose a fundraising project - something for the community like a local orphanage or a local retirement home and then also something to uplift the school. To uplift the school, the Lower Six Class of 2010 decided that they would like to honour and remember people who played a part in the development of the school.</p>
  <span class="more" style="left:802px;top:1234px">Read More</span>
</section>

<div class="abs rule" style="top:1304px"></div>

<section>
  <h2 class="abs cal-title">School <span>Calender</span></h2>
  <table class="abs cal">
    <thead><tr><th></th><th>First Term</th><th>Second Term</th><th>Third Term</th></tr></thead>
    <tbody>
      <tr><td class="label">Begins</td><td>Tuesday 14th January</td><td>Tuesday 13th May</td><td>Tuesday 9th September</td></tr>
      <tr><td class="label">1st Fixture Free</td><td>Friday 31st January –<br>Monday 3rd February</td><td>Friday 30th May –<br>Monday 2nd June</td><td>Friday 26th September –<br>Monday 29th September</td></tr>
      <tr><td class="label">Half-Term</td><td>Thursday 20th February –<br>Tuesday 25th February</td><td>Thursday 26th June –<br>Tuesday 1st July</td><td>Thursday 16th October –<br>Tuesday 21st October</td></tr>
      <tr><td class="label">2nd Fixture Free</td><td>Friday 14th March –<br>Monday 17th March</td><td>Friday 18th July –<br>Monday 21st July</td><td>Friday 7th November –<br>Monday 10th November</td></tr>
      <tr><td class="label">Term Ends</td><td>Thursday 10th April</td><td>Friday 7th August</td><td>Thursday 4th December</td></tr>
    </tbody>
  </table>
  <span class="btn-gold" style="left:312px">Download Registration Form</span>
  <span class="btn-gold" style="left:612px">2nd Term 2014 Termly Calendar</span>
</section>

<section>
  <h2 class="abs events-title">Upcoming <span>Events</span></h2>
  <div class="event" style="left:162px"><div class="pic" role="img" aria-label="Girls playing basketball" style="background:linear-gradient(#8a6a5a,#a4583a)"></div><h3>Fri 25 July 2014</h3><p>Basketball RISA Top Schools</p></div>
  <div class="event" style="left:388px"><div class="pic" role="img" aria-label="Pupils on a sports field" style="background:linear-gradient(#7a8a6a,#4d7a32)"></div><h3>Sat 02 Aug 2013</h3><p>School Play - Public Performance</p></div>
  <div class="event" style="left:612px"><div class="pic" role="img" aria-label="Students gathered outdoors" style="background:linear-gradient(#6a7a4a,#3f5a2f)"></div><h3>Thurs 07 Aug 2013</h3><p>Consultation for L6, 5B, L6, U6</p></div>

  <h2 class="abs sports-title">Sports <span>Announcements</span></h2>
  <ul class="abs sports"><li>- Rugby</li><li>- Hockey Boys</li><li>- Soccer</li><li>- Hockey Girls</li><li>- Basketball Girls</li></ul>

  <div class="partner" style="left:189px"><svg width="110" height="40"><rect width="110" height="40" fill="#1e4fa0"/></svg></div>
  <div class="partner" style="left:415px"><svg width="110" height="40"><rect width="110" height="40" fill="#e08a1e"/></svg></div>
  <div class="partner" style="left:637px"><svg width="60" height="60"><circle cx="30" cy="30" r="28" fill="#f2a31b"/></svg></div>
  <div class="partner" style="left:863px"><svg width="110" height="40"><rect width="110" height="40" fill="#c8282e"/></svg></div>
</section>

<footer>
  <div class="abs footer"></div>
  <div class="abs base"></div>
  <h2 class="abs" style="left:162px;top:2464px">Get in <span>Touch</span></h2>
  <div class="contact" style="left:152px;top:2510px">
    <div class="ic"><svg width="16" height="16" viewBox="0 0 16 16"><path d="M2 14V6l6-4 6 4v8z" fill="#0b5121"/></svg></div>
    <b>Brevanholt College</b>Lorem ipsum amet- 256894
  </div>
  <div class="contact" style="left:330px;top:2510px">
    <div class="ic"><svg width="14" height="18" viewBox="0 0 14 18"><path d="M7 17C3 11 1 9 1 6a6 6 0 0 1 12 0c0 3-2 5-6 11z" fill="#0b5121"/><circle cx="7" cy="6" r="2" fill="#f6e514"/></svg></div>
    <b>Map</b>Click here to see directions
  </div>
  <div class="contact" style="left:152px;top:2625px">
    <div class="ic"><svg width="16" height="16" viewBox="0 0 16 16"><path d="M3 1h3l1 4-2 1.5a9 9 0 0 0 4.5 4.5L11 9l4 1v3a2 2 0 0 1-2 2A12 12 0 0 1 1 3a2 2 0 0 1 2-2z" fill="#0b5121"/></svg></div>
    <b>Phone Number</b>0772406118 / 0771830462
  </div>
  <div class="contact" style="left:330px;top:2625px">
    <div class="ic"><svg width="18" height="14" viewBox="0 0 18 14"><rect x="1" y="1" width="16" height="12" fill="#0b5121"/><path d="M1 1l8 6 8-6" fill="none" stroke="#f6e514" stroke-width="1.3"/></svg></div>
    <b>Email Us</b>admin@brevanholt.example
  </div>

  <h2 class="abs" style="left:535px;top:2464px">Community <span>Feeds</span></h2>
  <div class="abs feed">
    <div class="head"><span class="sq"></span>Brevanholt School</div>
    <div class="like">1,076 people follow Brevanholt School</div>
    <div class="faces"><i></i><i></i><i></i><i></i><i></i><i></i><i></i><i></i><i></i><i></i></div>
  </div>

  <div class="abs signup">
    <h2>Signup <span>Newsletter</span></h2>
    <p>If you would like to be added to the list of parents that receive the School Newsletter, please enter your details below.</p>
    <div class="input">Enter Your Name</div>
    <div class="input">Enter Your Email</div>
    <div class="actions"><span class="sub">Subscribe</span><span class="unsub">Unsubscribe</span></div>
  </div>

  <div class="abs copy">2014 Brevanholt College. All Rights Reserved.</div>
  <div class="abs social"><i></i><i></i><i></i></div>
</footer>

</body>
</html>
```